Business Card Design Project for Electrical Company

We need a business card designed for a new Electrical Company called Dorvel Electrical Solutions, i dont mind if only Dorvel Electrical is used. We are a domestic and commercial Electrical Company that provides a range of Electrical Services. Our Company colours are Fluro Yellow and Black with the Lightning bolt picture attached.I have attached a card that has been made i think it is rather basic and am looking for something more. the font of Dorvel Electrical has been used on our car graphics as well as the lightning bolt. i want to keep them the same so we can brand our business. Some things we want on the front of the card are Dorvel Electrical Solutions, Owen Platt, 0438516274, admin@dorvelelectrical.example, Lic No 58342, Servicing CQ Region. But we want Owens name seperate to the phone number as its the phone number for the office, owen wont be answering the phone so we are thinking we dont want to give that impression. What do you think? with all that if you have complete different font designs please submit what you think would work best. keeping in mind our company name and details as well as coulors.

Industry/Entity Type

Business

```html
<!DOCTYPE html>
<html lang="en">
<head>
<meta charset="utf-8">
<title>Dorvel Electrical Solutions – Business Card</title>
<link rel="stylesheet" href="https://fonts.googleapis.com/css2?family=Source+Sans+3:wght@300;400;600;700&display=swap">
<style>
  :root {
    --fluro: #e4e600;
    --charcoal: #2b2a2c;
    --charcoal-soft: #3a393b;
    --paper: #ffffff;
    --ink: #333333;
    --ink-muted: #6a6a6a;
    --backdrop: #ecebe7;
    --services-text: #e9ea7a;
  }
  * { box-sizing: border-box; margin: 0; padding: 0; }
  html, body {
    width: 1200px; height: 1023px; overflow: hidden;
    background: var(--backdrop);
    font-family: "Source Sans 3", Arial, sans-serif;
  }
  .sheet {
    width: 1200px; height: 1023px;
    display: flex; flex-direction: column;
    align-items: center; justify-content: center; gap: 60px;
  }
  .card {
    position: relative; width: 720px; height: 412px;
    box-shadow: 0 8px 22px rgba(0,0,0,.18);
    overflow: hidden;
  }

  /* Front */
  .card-front { display: flex; background: var(--paper); }
  .front-brand {
    width: 300px; height: 100%;
    background: linear-gradient(160deg, var(--charcoal-soft) 0%, var(--charcoal) 60%, #1f1e20 100%);
    display: flex; align-items: center; justify-content: center;
    padding: 24px;
  }
  .wordmark {
    color: var(--fluro); font-weight: 700; text-transform: uppercase;
    line-height: 0.95; letter-spacing: 1px;
  }
  .wordmark span { display: block; }
  .front-brand .wordmark { font-size: 44px; }
  .front-details { position: relative; flex: 1; padding: 60px 44px 40px 44px; }
  .accent-tab {
    position: absolute; top: 0; right: 42px;
    width: 62px; height: 20px; background: var(--fluro);
  }
  .contact { font-size: 19px; color: var(--ink); line-height: 1.45; }
  .contact .licence { margin-bottom: 14px; }
  .contact b { font-weight: 700; display: inline-block; width: 64px; }
  .person { position: absolute; left: 44px; bottom: 44px; }
  .person-name { font-size: 30px; font-weight: 400; color: var(--ink-muted); }
  .person-role { font-size: 16px; font-weight: 300; color: var(--ink-muted); }

  /* Back */
  .card-back {
    background: radial-gradient(ellipse at 45% 40%, #f0f22c 0%, var(--fluro) 60%, #d8da00 100%);
  }
  .back-brand {
    position: absolute; left: 0; right: 0; top: 0; bottom: 92px;
    display: flex; align-items: center; justify-content: center;
  }
  .back-brand .wordmark { color: var(--charcoal); font-size: 62px; }
  .services {
    position: absolute; left: 0; right: 0; bottom: 0; height: 92px;
    background: var(--charcoal);
    display: grid; grid-template-columns: repeat(4, auto);
    grid-template-rows: repeat(2, auto);
    align-content: center; justify-content: space-around;
    row-gap: 6px; column-gap: 24px; padding: 0 30px;
    list-style: none;
  }
  .services li { font-size: 16px; color: var(--services-text); letter-spacing: .3px; }
</style>
</head>
<body>
<main class="sheet">
  <section class="card card-front" aria-label="Business card front">
    <div class="front-brand">
      <p class="wordmark"><span>Dorvel</span><span>Electrical</span><span>Solutions</span></p>
    </div>
    <div class="front-details">
      <div class="accent-tab"></div>
      <div class="contact">
        <p class="licence">Lic No 58342, Servicing CQ Region</p>
        <p><b>Phone:</b> 0438516274</p>
        <p><b>Email:</b> admin@dorvelelectrical.example</p>
      </div>
      <div class="person">
        <p class="person-name">Owen Platt</p>
        <p class="person-role">Licensed Electrician</p>
      </div>
    </div>
  </section>

  <section class="card card-back" aria-label="Business card back">
    <div class="back-brand">
      <p class="wordmark"><span>Dorvel</span><span>Electrical</span><span>Solutions</span></p>
    </div>
    <ul class="services">
      <li>Light &amp; Power</li>
      <li>Design &amp; Installation</li>
      <li>TV &amp; Data</li>
      <li>Renovations</li>
      <li>Test &amp; Tagging</li>
      <li>Air Con Installation</li>
      <li>Residential</li>
      <li>Smoke Detectors</li>
    </ul>
  </section>
</main>
</body>
</html>
```